Design Website for Data Entry

Design a single webpage website with three tabs, or section for. See the attached PDF for info. This webpage is a data entry dadshboard.

Target Market(s)

N/A

Number of Pages Required

3 page

Colors

Designer to choose colors to be used in the design.

```html
<!DOCTYPE html>
<html lang="en">
<head>
<meta charset="utf-8">
<title>Northgate – Messages</title>
<link rel="stylesheet" href="https://fonts.googleapis.com/css2?family=Montserrat:wght@400;500;600;700&display=swap">
<style>
  :root {
    --header-bg: #0a1c24;
    --page-bg: #0f2531;
    --card-bg: #0c222c;
    --card-border: #1d4252;
    --icon-bg: #224a5e;
    --label: #7a939e;
    --title: #ffffff;
    --footer-text: #6f8791;
    --rule: #1d3a47;
    --brand: #ffffff;
  }
  * { box-sizing: border-box; margin: 0; padding: 0; }
  html, body {
    width: 1200px;
    height: 1095px;
    overflow: hidden;
  }
  body {
    background: var(--page-bg);
    font-family: "Montserrat", sans-serif;
  }
  .site-header {
    height: 98px;
    background: var(--header-bg);
    border-bottom: 1px solid var(--rule);
    display: flex;
    align-items: center;
    justify-content: center;
    gap: 12px;
  }
  .brand-mark {
    width: 30px;
    height: 30px;
    background: var(--brand);
    border-radius: 6px;
  }
  .brand-name {
    color: var(--brand);
    font-weight: 700;
    font-size: 34px;
    letter-spacing: 0.5px;
  }
  .messages {
    padding: 46px 0 60px;
  }
  .messages-title {
    color: var(--title);
    font-weight: 500;
    font-size: 20px;
    line-height: 24px;
    text-align: center;
    margin-bottom: 37px;
    letter-spacing: 0.3px;
  }
  .message-list {
    width: 651px;
    margin: 0 0 0 263px;
    display: flex;
    flex-direction: column;
    gap: 19px;
  }
  .message-field {
    display: flex;
    height: 157px;
    background: var(--card-bg);
    border: 1px solid var(--card-border);
    border-radius: 3px;
    overflow: hidden;
  }
  .message-field.single-line { height: 46px; }
  .field-icon {
    width: 45px;
    flex: none;
    background: var(--icon-bg);
    display: flex;
    justify-content: center;
    padding-top: 12px;
  }
  .field-input {
    flex: 1;
    background: transparent;
    border: 0;
    resize: none;
    outline: none;
    padding: 13px 18px;
    font-family: "Montserrat", sans-serif;
    font-weight: 600;
    font-size: 15px;
    line-height: 20px;
    color: #d5e0e4;
  }
  .field-input::placeholder { color: var(--label); }
  .site-footer {
    border-top: 1px solid var(--rule);
    padding-top: 29px;
    text-align: center;
    color: var(--footer-text);
    font-size: 13px;
  }
</style>
</head>
<body>
  <header class="site-header">
    <span class="brand-mark"></span>
    <span class="brand-name">Northgate</span>
  </header>

  <main class="messages">
    <h1 class="messages-title">MESSAGES</h1>
    <div class="message-list">
      <label class="message-field">
        <span class="field-icon"><svg width="20" height="20" viewBox="0 0 24 24" fill="none" stroke="#fff" stroke-width="1.5" stroke-linejoin="round"><path d="M16.5 3.5l4 4L8 20l-5 1 1-5z"/><path d="M14 6l4 4"/><path d="M4 16l4 4"/></svg></span>
        <textarea class="field-input" placeholder="Welcome Message"></textarea>
      </label>
      <label class="message-field single-line">
        <span class="field-icon"><svg width="20" height="20" viewBox="0 0 24 24" fill="none" stroke="#fff" stroke-width="1.5" stroke-linejoin="round"><path d="M16.5 3.5l4 4L8 20l-5 1 1-5z"/><path d="M14 6l4 4"/><path d="M4 16l4 4"/></svg></span>
        <textarea class="field-input" rows="1" placeholder="Welcome Message Line"></textarea>
      </label>
      <label class="message-field">
        <span class="field-icon"><svg width="20" height="20" viewBox="0 0 24 24" fill="none" stroke="#fff" stroke-width="1.5" stroke-linejoin="round"><path d="M16.5 3.5l4 4L8 20l-5 1 1-5z"/><path d="M14 6l4 4"/><path d="M4 16l4 4"/></svg></span>
        <textarea class="field-input" placeholder="Quick Setup Disclaimer"></textarea>
      </label>
      <label class="message-field">
        <span class="field-icon"><svg width="20" height="20" viewBox="0 0 24 24" fill="none" stroke="#fff" stroke-width="1.5" stroke-linejoin="round"><path d="M16.5 3.5l4 4L8 20l-5 1 1-5z"/><path d="M14 6l4 4"/><path d="M4 16l4 4"/></svg></span>
        <textarea class="field-input" placeholder="Pop Up Message 1"></textarea>
      </label>
      <label class="message-field">
        <span class="field-icon"><svg width="20" height="20" viewBox="0 0 24 24" fill="none" stroke="#fff" stroke-width="1.5" stroke-linejoin="round"><path d="M16.5 3.5l4 4L8 20l-5 1 1-5z"/><path d="M14 6l4 4"/><path d="M4 16l4 4"/></svg></span>
        <textarea class="field-input" placeholder="Video Playlist Names"></textarea>
      </label>
    </div>
  </main>

  <footer class="site-footer">Copyright 2018 Northgate | All Rights Reserved</footer>
</body>
</html>
```